Playbill Ad Design

Hi, I need a single page ad designed 8" tall and 5" wide at 300dpi.

Requirements
-KSV Logo
-Phone Number - 800-372-KSV4
-Web site - www.kestrelvantagestudios.example
-Email - sales@kestrelvantagestudios.example

```html
<!DOCTYPE html>
<html lang="en">
<head>
<meta charset="utf-8">
<title>KSV Playbill Ad</title>
<link href="https://fonts.googleapis.com/css2?family=Archivo+Black&family=Permanent+Marker&family=Poppins:wght@400;600;700;800&family=Russo+One&display=swap" rel="stylesheet">
<style>
:root{
  --ink:#000;
  --white:#fff;
  --red:#ff1a2e;
  --pink:#ff1f7a;
  --magenta:#e0289b;
  --violet:#8a3cff;
  --blue:#2f6dff;
  --green:#3be03a;
  --orange:#ff9a2e;
}
*{margin:0;padding:0;box-sizing:border-box}
html,body{width:732px;height:1200px;overflow:hidden;background:var(--ink)}
.ad{position:relative;width:732px;height:1200px;background:var(--ink);overflow:hidden;font-family:'Poppins',sans-serif;color:var(--white)}

.photo{position:absolute;inset:0}
.photo-left-top{clip-path:polygon(0 0,160px 0,160px 455px,0 380px);
  background:radial-gradient(ellipse at 60% 10%,#ff1940 0%,#a2123c 35%,#5a1e63 65%,#2a0b2a 100%)}
.photo-left-low{clip-path:polygon(0 385px,160px 460px,160px 860px,0 860px);
  background:radial-gradient(ellipse at 70% 40%,#ff2a3d 0%,#a0102a 35%,#3a0812 70%,#120306 100%)}
.photo-stage{clip-path:polygon(160px 130px,550px 345px,550px 560px,160px 560px);
  background:linear-gradient(180deg,#2e2a24 0%,#3c3a30 35%,#5bd13a 60%,#1f5f18 80%,#0b0b0b 100%)}
.photo-camera{clip-path:polygon(162px 0,732px 0,732px 150px,585px 350px,162px 128px);
  background:radial-gradient(ellipse at 75% 45%,#2b3fbf 0%,#142276 40%,#080b2c 80%,#04040f 100%)}
.photo-concert{clip-path:polygon(732px 152px,732px 860px,540px 860px,540px 520px,587px 352px);
  background:radial-gradient(ellipse at 70% 30%,#ff3fb0 0%,#7a2fbf 30%,#231a52 60%,#07060f 100%)}
.fade{position:absolute;left:0;right:0;top:640px;height:240px;background:linear-gradient(180deg,rgba(0,0,0,0) 0%,#000 100%)}
.rules{position:absolute;inset:0}

.brand{position:absolute;top:58px;left:0;right:0;text-align:center;color:var(--white);font-family:'Poppins',sans-serif;font-weight:800}
.brand-mark{font-size:54px;line-height:1;letter-spacing:2px}
.brand-name{font-size:18px;font-weight:800;letter-spacing:1px;margin-top:2px}

.headline-panel{position:absolute;left:150px;top:352px;width:430px;height:370px;transform:rotate(-4deg);
  background:linear-gradient(160deg,#2a0620 0%,#000 45%,#000 100%);
  border-top:2px solid var(--violet);border-bottom:2px solid var(--blue);border-left:1px solid #333;border-right:1px solid #444}
.headline-art{position:absolute;inset:0;width:100%;height:100%;overflow:visible}
.h-elevate{font-family:'Archivo Black',sans-serif;font-size:72px;fill:#f2f2f2}
.h-the{font-family:'Russo One',sans-serif;font-size:24px;fill:var(--white)}
.h-script{font-family:'Permanent Marker',cursive}
.h-production{font-size:64px}
.h-experience{font-size:50px}

.intro{position:absolute;left:150px;top:752px;width:440px;transform:rotate(-5deg);font-size:14px;line-height:1.3;text-align:center}
.intro strong{color:var(--pink);font-weight:700}

.services{position:absolute;top:842px;left:60px;width:612px;display:flex}
.service{flex:1;text-align:center;position:relative}
.service + .service::before{content:"";position:absolute;left:0;top:0;height:148px;width:1px;background:#bbb}
.ring{width:104px;height:104px;border-radius:50%;margin:0 auto;border:3px solid;display:flex;align-items:center;justify-content:center}
.ring svg{width:58px;height:58px;fill:none;stroke-width:3;stroke-linecap:round;stroke-linejoin:round}
.ring-light{border-color:var(--red);box-shadow:0 0 14px var(--red)}
.ring-light svg{stroke:var(--red)}
.ring-sound{border-color:var(--pink);box-shadow:0 0 14px var(--pink)}
.ring-sound svg{stroke:var(--pink)}
.ring-video{border-color:var(--blue);box-shadow:0 0 14px var(--blue)}
.ring-video svg{stroke:var(--blue)}
.ring-stage{border-color:var(--green);box-shadow:0 0 14px var(--green)}
.ring-stage svg{stroke:var(--green);stroke-width:2}
.service-label{font-family:'Russo One',sans-serif;font-size:24px;margin-top:22px;letter-spacing:.5px}

.motto{position:absolute;left:79px;top:1019px;width:574px;height:38px;border:1.5px solid;border-image:linear-gradient(90deg,var(--red),var(--magenta)) 1}
.motto svg{display:block;width:100%;height:100%}
.motto text{font-family:'Archivo Black',sans-serif;font-size:16px;fill:var(--white)}

.phone{position:absolute;top:1073px;left:0;right:0;display:flex;align-items:center;justify-content:center;gap:12px}
.phone-icon{width:34px;height:34px;border-radius:50%;background:linear-gradient(135deg,var(--pink),var(--violet));display:flex;align-items:center;justify-content:center}
.phone-number{font-family:'Russo One',sans-serif;font-size:40px;background:linear-gradient(90deg,var(--red),var(--pink));-webkit-background-clip:text;background-clip:text;color:transparent}

.contact{position:absolute;top:1126px;left:0;right:0;display:flex;justify-content:center;align-items:center;gap:12px;font-size:13.5px;font-weight:600}
.contact svg{width:20px;height:20px;vertical-align:middle;margin-right:6px}
.sep{width:1px;height:20px;background:var(--pink)}
</style>
</head>
<body>
<div class="ad">
  <div class="photo photo-camera" role="img" aria-label="Photo of a broadcast camera operator filming a concert crowd in blue light"></div>
  <div class="photo photo-stage" role="img" aria-label="Photo of a ballroom stage with green lit set pieces and projection screen"></div>
  <div class="photo photo-left-top" role="img" aria-label="Photo of a building lit in red and pink at a New Year celebration"></div>
  <div class="photo photo-left-low" role="img" aria-label="Photo of a ceremony stage with red moving lights and banner"></div>
  <div class="photo photo-concert" role="img" aria-label="Photo of an arena event with pink and blue stage lighting and a crowd"></div>
  <div class="fade"></div>
  <svg class="rules" viewBox="0 0 732 1200" aria-hidden="true">
    <g stroke-width="2.5" fill="none">
      <line x1="160" y1="0" x2="160" y2="455" stroke="var(--orange)"/>
      <line x1="162" y1="128" x2="585" y2="350" stroke="#ffd9a0"/>
      <line x1="732" y1="152" x2="587" y2="352" stroke="#ffc07a"/>
      <line x1="0" y1="380" x2="160" y2="456" stroke="#ffe2e8"/>
    </g>
  </svg>

  <div class="brand">
    <div class="brand-mark">KSV</div>
    <div class="brand-name">kestrel vantage studios</div>
  </div>

  <div class="headline-panel">
    <svg class="headline-art" viewBox="0 0 430 370" role="img" aria-label="Elevate the production experience">
      <defs>
        <linearGradient id="grad-production" x1="0" x2="1" y1="0" y2="0">
          <stop offset="0" stop-color="#ff4a8a"/><stop offset="1" stop-color="#ff1f6a"/>
        </linearGradient>
        <linearGradient id="grad-experience" x1="0" x2="1" y1="0" y2="0">
          <stop offset="0" stop-color="#c02ad0"/><stop offset=".5" stop-color="#6a4cff"/><stop offset="1" stop-color="#2f6dff"/>
        </linearGradient>
      </defs>
      <text class="h-elevate" x="40" y="102" textLength="350" lengthAdjust="spacingAndGlyphs">ELEVATE</text>
      <rect x="118" y="134" width="40" height="4" fill="var(--pink)"/>
      <rect x="272" y="134" width="40" height="4" fill="var(--pink)"/>
      <text class="h-the" x="170" y="145" textLength="90" lengthAdjust="spacing">THE</text>
      <g transform="skewX(-8) translate(30 0)">
        <text class="h-script h-production" x="30" y="232" textLength="360" lengthAdjust="spacingAndGlyphs" fill="url(#grad-production)">PRODUCTION</text>
        <text class="h-script h-experience" x="95" y="300" textLength="270" lengthAdjust="spacingAndGlyphs" fill="url(#grad-experience)">EXPERIENCE</text>
      </g>
    </svg>
  </div>

  <p class="intro">THE Lighting, Sound, Video &amp; Staging for<br>corporate events, concerts, galas and <strong>unforgettable</strong><br><strong>live experiences.</strong></p>

  <div class="services">
    <div class="service">
      <div class="ring ring-light"><svg viewBox="0 0 60 60"><path d="M22 38c-4-3-6-7-6-11a14 14 0 0 1 28 0c0 4-2 8-6 11v6H22z"/><path d="M24 50h12"/><path d="M30 4v5M10 27H5M55 27h-5M14 11l3 3M46 11l-3 3M14 43l3-3M46 43l-3-3"/></svg></div>
      <div class="service-label">LIGHTING</div>
    </div>
    <div class="service">
      <div class="ring ring-sound"><svg viewBox="0 0 60 60"><rect x="14" y="4" width="32" height="52" rx="2"/><circle cx="30" cy="18" r="7"/><circle cx="30" cy="40" r="10"/><circle cx="41" cy="30" r="1.5"/></svg></div>
      <div class="service-label">SOUND</div>
    </div>
    <div class="service">
      <div class="ring ring-video"><svg viewBox="0 0 60 60"><circle cx="30" cy="30" r="25"/><path d="M24 19l16 11-16 11z"/></svg></div>
      <div class="service-label">VIDEO</div>
    </div>
    <div class="service">
      <div class="ring ring-stage"><svg viewBox="0 0 60 60"><path d="M6 8l8 3v14H6zM54 8l-8 3v14h8zM14 13h32M14 22h32M4 28h52M4 32h52"/><circle cx="12" cy="40" r="3"/><circle cx="24" cy="40" r="3"/><circle cx="36" cy="40" r="3"/><circle cx="48" cy="40" r="3"/><path d="M6 52v-5h12v5M18 52v-5h12v5M30 52v-5h12v5M42 52v-5h12v5"/></svg></div>
      <div class="service-label">STAGING</div>
    </div>
  </div>

  <div class="motto">
    <svg viewBox="0 0 571 35" aria-label="Production. Power. Perfection.">
      <text x="20" y="24" textLength="531" lengthAdjust="spacing">PRODUCTION.POWER.PERFECTION.</text>
    </svg>
  </div>

  <div class="phone">
    <div class="phone-icon"><svg width="18" height="18" viewBox="0 0 24 24" fill="#fff"><path d="M6.6 10.8a15 15 0 0 0 6.6 6.6l2.2-2.2c.3-.3.7-.4 1-.2 1.1.4 2.3.6 3.6.6.6 0 1 .4 1 1V20c0 .6-.4 1-1 1A17 17 0 0 1 3 4c0-.6.4-1 1-1h3.5c.6 0 1 .4 1 1 0 1.3.2 2.5.6 3.6.1.3 0 .7-.2 1z"/></svg></div>
    <div class="phone-number">800-372-KSV4</div>
  </div>

  <div class="contact">
    <span><svg viewBox="0 0 24 24" fill="none" stroke="var(--violet)" stroke-width="2"><circle cx="12" cy="12" r="10"/><path d="M2 12h20M12 2c3 3 3 17 0 20M12 2c-3 3-3 17 0 20"/></svg>www.kestrelvantagestudios.example</span>
    <span class="sep"></span>
    <span><svg viewBox="0 0 24 24" fill="none" stroke="var(--violet)" stroke-width="2"><rect x="2" y="5" width="20" height="14"/><path d="M2 5l10 8 10-8"/></svg>sales@kestrelvantagestudios.example</span>
  </div>
</div>
</body>
</html>
```